VORELLA MILK

The packaging is to package milk. The product will be on the shelf of supermarkets. the visual identity should reflect a global product. to milk the color red must prevail. the logo, preferably should be vertically. In packaging the logo should be easy reading. know that it is prohibited to place the flag of a country on the packaging. however, we suggest that you create small symbols that can remember the flag of italy, switzerland, germany and the united states. In the attached technical drawing of Plenox Cart. The logo. A photo 3 dimensions of the package. Good luck
Updates

1 - statement of the parties : the design of the packaging has 15 parties. Let us enumerate every piece of 1 to 15. where 6 is the black arrows is part number 1 (DATA DE FABRICAÇÃO/LOTE/ VÁLIDO ATÉ:) . which is in Portuguese " LEVANTE RASGUE OU CORTE " is the part number 2 . going in that direction is the number 3 , 4 , 5 . Below we part 6 (which is one half of the main panel 8 ) 7 , the part 8 is the main panel . and so on until part 15 .
2 - indication measurements : Part 1 ( 47mm width x 38mm height) , Part 2 ( 62mm width x 38mm height) , Part 3 ( 94mm width x 38mm height) , part 4 ( 62mm width x 38mm height) , Part 5 ( 47mm width x 38mm height) , Part 6 ( 47mm width x 167mm height) , Part 7 ( 62mm width x 167mm height) , part 8 ( 94mm width x 167mm height) , part 9 ( 62mm width x 167mm height) , part 10 ( 47mm 167mm width X height) , part 11 ( 47mm width x 38mm height) , part 12 ( 62mm width x 38mm height) , part 13 ( 94mm width x 38mm height) , part 14 ( 62mm width x 38mm height) , part 15 ( 47mm 38mm width X height) 3.Part 8: these are the words in Portuguese: 
part 8
The logo must be 12mmx65mm
3 This words with 10mm height X 50mm width: LEITE UHT INTEGRAL.

This box with 11mm height X 65mm width at the bottom of the main panel near 1L. "AVISO IMPORTANTE: ESTE PRODUTO NÃO DEVE SER USADO PARA ALIMENTAR CRIANÇAS MENORES DE 1(UM) ANO DE IDADE, A NÃO SER POR INDICAÇÃO EXPRESSA DE MÉDICO OU NUTRICIONISTA. O ALEITAMENTO MATERNO EVITA INFECÇÕES E ALERGIAS E DEVE SER MANTIDO ATÉ A CRIANÇA COMPLETAR 2(DOIS) ANOS DE IDADE"

part 7

INFORMAÇÃO NUTRICIONAL

Porção de 200ml (1 copo)

Quantidade por porção   %VD (*)

Valor energético  118cal=496KJ   6

Carboidratos            10g               3

Proteinas                   6,2g             8

Gorduras totais          6,0g            11

Gorduras saturadas    3,7g           17

Gorduras trans             0           VD não estabelecido

Fibra alimentar            0                0

Sódio                        143mg         6

Cálcio                        240mg       24

*% Valores Diários com base em uma dieta de 2.000 Kcal ou 8.400KJ.

Seus valores diários podem ser maiores ou menores dependendo de suas necessidades energéticas.

************************

NÃO CONTÉM GLÚTEN

***************************

NÃO NECESSITA DE REFRIGERAÇÃO.

APÓS ABERTO, CONSERVAR EM

GELADEIRA (1 A 10°C) POR ATÉ 3 DIAS.

Ingredientes: leite integral, estabilizantes citrato de sodio, difosfato de sodio, trifosfato de sodio.

part 9

O Leite integral Vorella é ultrapasteurizado

por tratamento térmico especial -UHT(Ultra 

High Temperatura), aquecido a 135 °C/145°C

por um período de 2 a 4 segundos e resfriado

rapidamente. É envasado nesta embalagem asséptica,

impermeável ao ar, à luz e aos germes. Este processo

garante um leite sem bactérias, conservando o seu 

sabor e propriedades nutritivas. 

*********************************************************

PRODUZIDO POR:

TuDVAN do Brasil LTDA

Usina de Beneficiamento

Rua Alvorada dos Pinhais 47

CEP 47.610-000, Frutal-MG

CNPJ 58.143.902/0007-31

Registro no Ministério  da

Agricultura SIF/DIPOA sob 

o n° 0008/5261

           DISTRIBUÍDO POR:

TuDVAN do Brasil LTDA.

         INDUSTRIA BRASILEIRA

 *********************************        

MINISTÉRIO DA AGRICULTURA

BRASIL

INSPECIONADO

5261

S.I.F.

```html
<!DOCTYPE html>
<html lang="pt">
<head>
<meta charset="utf-8">
<title>Vorella Milk – carton front and side panel</title>
<link rel="stylesheet" href="https://fonts.googleapis.com/css2?family=Varela+Round&family=Nunito:wght@700&family=Roboto+Condensed:wght@400;700&display=swap">
<style>
  :root {
    --page: #ffffff;
    --sky: #3cc3e6;
    --sky-mid: #6fd2ee;
    --sky-light: #a6e3f3;
    --sky-side: #35b4d8;
    --white: #ffffff;
    --red: #ec2a35;
    --logo-blue: #2a6fb4;
    --ink: #1d2a33;
    --mark-green: #2e9b46;
    --mark-black: #111111;
    --mark-gold: #f5c400;
    --mark-navy: #2b3b7e;
  }
  * { box-sizing: border-box; margin: 0; padding: 0; }
  html, body { width: 832px; height: 1200px; overflow: hidden; background: var(--page); }
  body { position: relative; font-family: "Varela Round", sans-serif; }

  .carton { position: absolute; left: 106px; top: 120px; width: 620px; height: 960px; }

  /* top flap */
  .top-flap {
    position: absolute; left: 150px; top: 0; width: 470px; height: 40px;
    background: var(--sky-light); overflow: hidden;
  }
  .top-flap__word {
    position: absolute; left: 0; right: 0; top: 1px; text-align: center;
    color: var(--red); font-family: "Nunito", sans-serif; font-weight: 700;
    font-size: 40px; line-height: 36px; transform: rotate(180deg);
  }

  /* side panel */
  .side-panel {
    position: absolute; left: 0; top: 40px; width: 150px; height: 920px;
    background: var(--sky-side); padding: 14px 10px; color: var(--ink);
    font-family: "Roboto Condensed", sans-serif;
  }
  .side-panel__badge {
    display: block; width: 74px; height: 74px; margin: 30px auto 16px;
    border-radius: 50%; background: radial-gradient(circle, var(--white), var(--sky-light));
  }
  .nutrition { background: var(--white); padding: 5px; font-size: 7px; line-height: 1.3; }
  .nutrition__title { font-weight: 700; font-size: 8px; border-bottom: 1px solid var(--ink); }
  .nutrition table { width: 100%; border-collapse: collapse; }
  .nutrition td { border-bottom: 0.5px solid var(--ink); padding: 1px 0; }
  .nutrition td + td { text-align: right; }
  .nutrition__note { margin-top: 3px; font-size: 6px; }
  .side-panel__info { margin-top: 10px; font-size: 7px; line-height: 1.35; color: var(--white); font-weight: 700; }

  /* front panel */
  .front-panel {
    position: absolute; left: 150px; top: 40px; width: 470px; height: 920px;
    background: linear-gradient(180deg, var(--sky) 0%, var(--sky-mid) 60%, var(--sky-light) 100%);
    overflow: hidden;
  }
  .front-panel__crest { position: absolute; left: 0; top: 0; width: 470px; height: 220px; }
  .brand {
    position: absolute; left: 60px; right: 0; top: 62px;
    display: flex; flex-direction: column; align-items: center; gap: 12px;
  }
  .brand__dot { width: 58px; height: 58px; border-radius: 50%; background: var(--logo-blue); }
  .brand__name { color: var(--logo-blue); font-size: 40px; line-height: 1; }

  .milk-pour {
    position: absolute; left: 150px; top: 120px; width: 320px; height: 760px;
    background:
      radial-gradient(ellipse 55% 22% at 55% 86%, rgba(255,255,255,0.95), rgba(255,255,255,0) 100%),
      radial-gradient(ellipse 12% 60% at 62% 35%, rgba(255,255,255,0.75), rgba(255,255,255,0) 100%);
  }

  .product-word {
    position: absolute; left: 226px; top: 200px; width: 660px;
    transform-origin: 0 0; transform: rotate(90deg);
    color: var(--red); font-family: "Nunito", sans-serif; font-weight: 700;
    font-size: 300px; line-height: 150px; letter-spacing: 4px; white-space: nowrap;
  }

  .product-type {
    position: absolute; right: 18px; top: 778px;
    color: var(--red); font-family: "Nunito", sans-serif; font-weight: 700;
    font-size: 24px; line-height: 26px; letter-spacing: 0.5px;
  }
  .notice {
    position: absolute; left: 20px; right: 20px; top: 814px; height: 56px;
    background: var(--white); border: 1.5px solid var(--red); padding: 4px 6px;
    font-family: "Roboto Condensed", sans-serif; font-size: 6.6px; line-height: 1.3;
    color: var(--ink); text-align: justify;
  }
  .notice strong { color: var(--red); }

  .origin-band {
    position: absolute; left: 0; bottom: 0; width: 470px; height: 40px;
    background: var(--red); display: flex; align-items: center; padding: 0 14px;
  }
  .origin-band__volume { color: var(--white); font-size: 17px; flex: 1; }
  .origin-marks { display: flex; align-items: center; gap: 10px; }
  .origin-mark { display: flex; gap: 2px; }
  .origin-mark span { width: 8px; height: 8px; border-radius: 50%; border: 1px solid var(--white); }
  .origin-marks svg { display: block; }
</style>
</head>
<body>
<main class="carton" aria-label="Vorella Milk carton">
  <div class="top-flap"><div class="top-flap__word">milk</div></div>

  <aside class="side-panel">
    <span class="side-panel__badge" role="img" aria-label="Fresh milk illustrated badge"></span>
    <section class="nutrition">
      <p class="nutrition__title">INFORMAÇÃO NUTRICIONAL</p>
      <p>Porção de 200ml (1 copo)</p>
      <table>
        <tr><td>Valor energético</td><td>118cal 6</td></tr>
        <tr><td>Carboidratos</td><td>10g 3</td></tr>
        <tr><td>Proteínas</td><td>6,2g 8</td></tr>
        <tr><td>Gorduras totais</td><td>6,0g 11</td></tr>
        <tr><td>Gorduras saturadas</td><td>3,7g 17</td></tr>
        <tr><td>Gorduras trans</td><td>0</td></tr>
        <tr><td>Fibra alimentar</td><td>0 0</td></tr>
        <tr><td>Sódio</td><td>143mg 6</td></tr>
        <tr><td>Cálcio</td><td>240mg 24</td></tr>
      </table>
      <p class="nutrition__note">*% Valores Diários com base em uma dieta de 2.000 Kcal ou 8.400KJ.</p>
    </section>
    <p class="side-panel__info">NÃO CONTÉM GLÚTEN<br>NÃO NECESSITA DE REFRIGERAÇÃO. APÓS ABERTO, CONSERVAR EM GELADEIRA (1 A 10°C) POR ATÉ 3 DIAS.</p>
  </aside>

  <section class="front-panel">
    <svg class="front-panel__crest" viewBox="0 0 470 220" aria-hidden="true">
      <path d="M60 0 H470 V150 C420 200 340 222 250 215 C150 208 80 140 60 0 Z" fill="#ffffff"/>
    </svg>
    <div class="brand">
      <span class="brand__dot"></span>
      <span class="brand__name">Vorella</span>
    </div>
    <div class="milk-pour" role="img" aria-label="Stream of milk pouring down and splashing"></div>
    <div class="product-word">milk</div>

    <p class="product-type">LEITE UHT INTEGRAL</p>
    <p class="notice"><strong>AVISO IMPORTANTE:</strong> ESTE PRODUTO NÃO DEVE SER USADO PARA ALIMENTAR CRIANÇAS MENORES DE 1(UM) ANO DE IDADE, A NÃO SER POR INDICAÇÃO EXPRESSA DE MÉDICO OU NUTRICIONISTA. O ALEITAMENTO MATERNO EVITA INFECÇÕES E ALERGIAS E DEVE SER MANTIDO ATÉ A CRIANÇA COMPLETAR 2(DOIS) ANOS DE IDADE.</p>

    <div class="origin-band">
      <span class="origin-band__volume">1 litre</span>
      <div class="origin-marks">
        <svg width="16" height="16" viewBox="0 0 16 16" aria-label="Switzerland symbol"><circle cx="8" cy="8" r="7.5" fill="#fff"/><rect x="6.5" y="3.5" width="3" height="9" fill="var(--red)"/><rect x="3.5" y="6.5" width="9" height="3" fill="var(--red)"/></svg>
        <div class="origin-mark" aria-label="Germany symbol"><span style="background:var(--mark-black)"></span><span style="background:var(--red)"></span><span style="background:var(--mark-gold)"></span></div>
        <div class="origin-mark" aria-label="Italy symbol"><span style="background:var(--mark-green)"></span><span style="background:var(--white)"></span><span style="background:var(--red)"></span></div>
        <svg width="16" height="16" viewBox="0 0 16 16" aria-label="United States symbol"><circle cx="8" cy="8" r="7.5" fill="var(--mark-navy)" stroke="#fff"/><path d="M8 3.5l1.1 3.1h3.2l-2.6 1.9 1 3.1L8 9.7l-2.7 1.9 1-3.1-2.6-1.9h3.2z" fill="#fff"/></svg>
      </div>
    </div>
  </section>
</main>
</body>
</html>
```